Business Card Design Project

We need a simple business card design that uses our current logo.
We need to have the current logo put into a high res format.
We need to have 1 card made with contact information.
We will supply the information for the 4 employees.
Industry/Entity Type
Business
Requirements
Must have
- The contact information is as follows:
Paul Vardenko
Producer/CEO
c. 949-555-0148
f. 650-555-0193
paulv@lanternyardstudio.example
Mel Trosgaard, CFO
c. 949-555-0172
f. 650-555-0193
melt@lanternyardstudio.example
Paul Brenneky, PR
c. 267-555-0126
f. 650-555-0193
pbrenneky@lanternyardstudio.example
Dale Furnow, Producer
c. 949-555-0164
f. 650-555-0193
dalef@lanternyardstudio.example
The address for all cards is:
318 W Calle Norvista #2715, San Clemente, CA 92631

```html
<!DOCTYPE html>
<html lang="en">
<head>
<meta charset="utf-8">
<title>Lantern Yard Studio — Business Cards</title>
<link rel="stylesheet" href="https://fonts.googleapis.com/css2?family=Source+Sans+3:wght@400;600;700&display=swap">
<style>
  :root {
    --canvas-bg: #ffffff;
    --card-blue: #1ab0e0;
    --card-blue-deep: #13a6d8;
    --frame-line: rgba(255,255,255,0.75);
    --sheen-tone: rgba(255,255,255,0.14);
    --badge-fill: rgba(255,255,255,0.16);
    --name-ink: #10233a;
    --detail-ink: #ffffff;
    --brand-ink: #0d2440;
  }
  html, body {
    margin: 0;
    padding: 0;
    overflow: hidden;
  }
  body {
    width: 1179px;
    height: 1200px;
    background: var(--canvas-bg);
    position: relative;
    font-family: "Source Sans 3", "Myriad Pro", sans-serif;
  }
  .card {
    position: absolute;
    width: 497px;
    height: 298px;
    background: linear-gradient(160deg, var(--card-blue) 0%, var(--card-blue-deep) 100%);
    overflow: hidden;
  }
  .card-frame {
    position: absolute;
    inset: 0;
    width: 100%;
    height: 100%;
  }
  .card-sheen {
    position: absolute;
    left: 0;
    right: 0;
    bottom: 0;
    height: 70px;
    background: linear-gradient(180deg, rgba(255,255,255,0) 0%, var(--sheen-tone) 100%);
  }
  .card--front { left: 13px; top: 232px; }
  .card--vardenko { left: 13px; top: 556px; }
  .card--trosgaard { left: 597px; top: 61px; }
  .card--brenneky { left: 597px; top: 392px; }
  .card--furnow { left: 597px; top: 713px; }

  .brand-name {
    position: absolute;
    left: 0;
    right: 0;
    top: 122px;
    text-align: center;
    font-weight: 700;
    font-size: 38px;
    line-height: 1;
    letter-spacing: 1px;
    color: var(--brand-ink);
    margin: 0;
  }
  .brand-address {
    position: absolute;
    left: 0;
    right: 0;
    top: 186px;
    text-align: center;
    font-size: 15px;
    font-weight: 400;
    color: var(--detail-ink);
    margin: 0;
  }

  .person-name {
    position: absolute;
    left: 44px;
    top: 46px;
    margin: 0;
    font-size: 34px;
    font-weight: 400;
    color: var(--name-ink);
    line-height: 1;
  }
  .person-title {
    position: absolute;
    left: 46px;
    top: 86px;
    margin: 0;
    font-size: 17px;
    font-weight: 400;
    color: var(--name-ink);
    line-height: 1.2;
  }
  .person-contact {
    position: absolute;
    left: 46px;
    top: 205px;
    margin: 0;
    padding: 0;
    list-style: none;
    font-size: 15px;
    line-height: 21px;
    color: var(--detail-ink);
    font-weight: 400;
  }
</style>
</head>
<body>

  <section class="card card--front" aria-label="Company card">
    <div class="card-sheen" role="img" aria-label="Soft light sweep along the lower edge"></div>
    <svg class="card-frame" viewBox="0 0 497 298" aria-hidden="true">
      <rect x="16" y="16" width="465" height="266" rx="22" fill="none" stroke="var(--frame-line)" stroke-width="1.5"/>
    </svg>
    <h1 class="brand-name">LANTERN YARD STUDIO</h1>
    <p class="brand-address">318 W Calle Norvista #2715, San Clemente, CA 92631</p>
  </section>

  <section class="card card--vardenko" aria-label="Paul Vardenko card">
    <div class="card-sheen" role="img" aria-label="Soft light sweep along the lower edge"></div>
    <svg class="card-frame" viewBox="0 0 497 298" aria-hidden="true">
      <rect x="16" y="16" width="465" height="266" rx="22" fill="none" stroke="var(--frame-line)" stroke-width="1.5"/>
      <circle cx="352" cy="116" r="92" fill="var(--badge-fill)"/>
    </svg>
    <h2 class="person-name">Paul Vardenko</h2>
    <p class="person-title">Producer/CEO</p>
    <ul class="person-contact">
      <li>c. 949-555-0148</li>
      <li>f. 650-555-0193</li>
      <li>paulv@lanternyardstudio.example</li>
    </ul>
  </section>

  <section class="card card--trosgaard" aria-label="Mel Trosgaard card">
    <div class="card-sheen" role="img" aria-label="Soft light sweep along the lower edge"></div>
    <svg class="card-frame" viewBox="0 0 497 298" aria-hidden="true">
      <rect x="16" y="16" width="465" height="266" rx="22" fill="none" stroke="var(--frame-line)" stroke-width="1.5"/>
      <circle cx="352" cy="114" r="92" fill="var(--badge-fill)"/>
    </svg>
    <h2 class="person-name">Mel Trosgaard</h2>
    <p class="person-title">CFO</p>
    <ul class="person-contact">
      <li>c. 949-555-0172</li>
      <li>f. 650-555-0193</li>
      <li>melt@lanternyardstudio.example</li>
    </ul>
  </section>

  <section class="card card--brenneky" aria-label="Paul Brenneky card">
    <div class="card-sheen" role="img" aria-label="Soft light sweep along the lower edge"></div>
    <svg class="card-frame" viewBox="0 0 497 298" aria-hidden="true">
      <rect x="16" y="16" width="465" height="266" rx="22" fill="none" stroke="var(--frame-line)" stroke-width="1.5"/>
      <circle cx="352" cy="114" r="92" fill="var(--badge-fill)"/>
    </svg>
    <h2 class="person-name">Paul Brenneky</h2>
    <p class="person-title">PR</p>
    <ul class="person-contact">
      <li>c. 267-555-0126</li>
      <li>f. 650-555-0193</li>
      <li>pbrenneky@lanternyardstudio.example</li>
    </ul>
  </section>

  <section class="card card--furnow" aria-label="Dale Furnow card">
    <div class="card-sheen" role="img" aria-label="Soft light sweep along the lower edge"></div>
    <svg class="card-frame" viewBox="0 0 497 298" aria-hidden="true">
      <rect x="16" y="16" width="465" height="266" rx="22" fill="none" stroke="var(--frame-line)" stroke-width="1.5"/>
      <circle cx="352" cy="114" r="92" fill="var(--badge-fill)"/>
    </svg>
    <h2 class="person-name">Dale Furnow</h2>
    <p class="person-title">Producer</p>
    <ul class="person-contact">
      <li>c. 949-555-0164</li>
      <li>f. 650-555-0193</li>
      <li>dalef@lanternyardstudio.example</li>
    </ul>
  </section>

</body>
</html>
```